Signage for a store*

logo on the two sides of the sign
in the middle is the name of the store witch is KORVELO
at the bottom of the two logos, one side for location/address and the other side is contact details phone number is 718-392-6170 address is 7342 THE SIGN WILL BEE 15 FEET BY 4 FEET I WOULD LIKE THAT THE
BACKGROUND OF THE SIGN SHOULD HAVE A NICE COLOR BASE
THAT GOES FOR A WINE STORE

```html
<!DOCTYPE html>
<html lang="en">
<head>
<meta charset="UTF-8">
<title>KORVELO Wine Store Sign</title>
<link href="https://fonts.googleapis.com/css2?family=Courier+Prime&family=Old+Standard+TT&display=swap" rel="stylesheet">
<style>
  :root {
    --sign-bg: #000000;
    --gold: #b5871a;
    --wine: #a3173c;
  }
  html, body {
    margin: 0;
    padding: 0;
    overflow: hidden;
    background: var(--sign-bg);
  }
  .sign {
    position: relative;
    width: 1200px;
    height: 320px;
    background: var(--sign-bg);
    overflow: hidden;
  }
  .brand-mark {
    position: absolute;
    top: 76px;
    width: 140px;
    height: 112px;
    display: flex;
    flex-direction: column;
    align-items: center;
    justify-content: center;
    gap: 10px;
  }
  .brand-mark--left { left: 44px; }
  .brand-mark--right { left: 1000px; }
  .brand-mark__circle {
    width: 46px;
    height: 46px;
    border: 2px solid var(--wine);
    border-radius: 50%;
    box-sizing: border-box;
  }
  .brand-mark__name {
    font-family: "Old Standard TT", serif;
    font-size: 22px;
    color: var(--wine);
    letter-spacing: 0.04em;
    line-height: 1;
    white-space: nowrap;
  }
  .store-name {
    position: absolute;
    left: 232px;
    top: 64px;
    width: 700px;
    margin: 0;
    text-align: center;
    font-family: "Courier Prime", monospace;
    font-weight: 400;
    font-size: 166px;
    line-height: 1;
    color: var(--gold);
    letter-spacing: 0;
    white-space: nowrap;
    transform: scaleX(0.82);
    transform-origin: center;
  }
  .store-type {
    position: absolute;
    left: 320px;
    top: 216px;
    width: 548px;
    height: 36px;
    display: flex;
    align-items: center;
    justify-content: space-between;
  }
  .store-type__rule {
    width: 114px;
    height: 1.5px;
    background: var(--wine);
  }
  .store-type__label {
    font-family: "Old Standard TT", serif;
    font-size: 36px;
    color: var(--gold);
    letter-spacing: 0.16em;
    transform: scaleX(0.82);
    line-height: 1;
    white-space: nowrap;
  }
  .detail {
    position: absolute;
    top: 220px;
    margin: 0;
    width: 260px;
    text-align: center;
    font-family: "Old Standard TT", serif;
    font-size: 28px;
    color: var(--gold);
    letter-spacing: 0.08em;
    line-height: 1;
    white-space: nowrap;
    transform: scaleX(0.85);
    transform-origin: center;
  }
  .detail--address { left: -16px; }
  .detail--phone { left: 940px; }
</style>
</head>
<body>
  <div class="sign">
    <div class="brand-mark brand-mark--left">
      <span class="brand-mark__circle"></span>
      <span class="brand-mark__name">KORVELO</span>
    </div>

    <h1 class="store-name">KORVELO</h1>

    <div class="store-type">
      <span class="store-type__rule"></span>
      <span class="store-type__label">WINE STORE</span>
      <span class="store-type__rule"></span>
    </div>

    <div class="brand-mark brand-mark--right">
      <span class="brand-mark__circle"></span>
      <span class="brand-mark__name">KORVELO</span>
    </div>

    <p class="detail detail--address">7342</p>
    <p class="detail detail--phone">718-392-6170</p>
  </div>
</body>
</html>
```